Pelican Crest landing page design

We need a landing page designed for an ecommerce website that sales fresh US domestic shrimp from the Gulf of Mexico and ships them direct to the consumer "From Our Shore To Your Door". For the landing page, we would like customers to be able to place an order and or inquire further about our product as well as links to social media. The company logo is attached

1 page

```html
<!DOCTYPE html>
<html lang="en">
<head>
<meta charset="utf-8">
<title>Pelican Crest – Fresh Gulf Shrimp</title>
<link rel="stylesheet" href="https://fonts.googleapis.com/css2?family=Poppins:wght@400;500;600;700&family=Open+Sans:wght@400;600&family=Oswald:wght@500&display=swap">
<style>
  :root {
    --white: #ffffff;
    --ink: #1b1b1b;
    --body-text: #555555;
    --steel: #8aa5c0;
    --steel-dark: #7c98b4;
    --mist: #e7ebee;
    --mist-deep: #d9dfe4;
    --buy-red: #d8232a;
    --shrimp-light: #f4c9a4;
    --shrimp: #e88a55;
    --shrimp-deep: #b8562f;
    --line: #d6dde3;
  }
  * { margin: 0; padding: 0; box-sizing: border-box; }
  html, body { width: 698px; height: 1200px; overflow: hidden; background: var(--white); }
  body { position: relative; font-family: "Open Sans", Arial, sans-serif; color: var(--ink); }

  /* Header */
  .site-header { position: absolute; top: 0; left: 0; width: 698px; height: 64px; background: var(--white); }
  .brand { position: absolute; left: 65px; top: 5px; display: flex; align-items: center; gap: 8px; }
  .brand-mark { width: 54px; height: 54px; border: 1.5px solid var(--steel); border-radius: 50%; }
  .brand-name { font-family: "Poppins", Arial, sans-serif; font-weight: 600; font-size: 17px; letter-spacing: 1px; color: #333333; }
  .main-nav { position: absolute; top: 25px; left: 346px; display: flex; gap: 0; font-family: "Poppins", Arial, sans-serif; font-weight: 600; font-size: 9.5px; }
  .main-nav a { color: var(--ink); text-decoration: none; margin-right: 30px; }
  .cart-icon { position: absolute; left: 621px; top: 26px; }

  /* Hero */
  .hero { position: absolute; top: 64px; left: 0; width: 698px; height: 341px; overflow: hidden; }
  .hero-photo { position: absolute; inset: 0;
    background: radial-gradient(ellipse at 30% 40%, var(--shrimp-light) 0%, var(--shrimp) 35%, transparent 65%),
                radial-gradient(ellipse at 75% 60%, var(--shrimp-light) 0%, var(--shrimp) 40%, var(--shrimp-deep) 80%),
                var(--shrimp); }
  .hero-title { position: absolute; top: 96px; width: 100%; text-align: center; font-family: "Poppins", Arial, sans-serif; font-weight: 700; font-size: 50px; line-height: 52px; color: var(--white); letter-spacing: 1px; }
  .hero-button { position: absolute; left: 292px; top: 210px; width: 114px; height: 26px; border-radius: 13px; background: var(--steel); color: var(--white); font-family: "Poppins", Arial, sans-serif; font-weight: 600; font-size: 10.5px; line-height: 26px; text-align: center; }
  .slider-dots { position: absolute; top: 303px; left: 314px; display: flex; gap: 10px; }
  .slider-dots span { width: 10px; height: 10px; border-radius: 50%; border: 1.5px solid var(--white); }
  .slider-dots span.is-active { background: var(--white); }

  /* Products */
  .products { position: absolute; top: 405px; left: 0; width: 698px; height: 529px; overflow: hidden; }
  .products-backdrop { position: absolute; inset: 0; background: linear-gradient(180deg, var(--mist) 0%, var(--mist-deep) 60%, var(--mist) 100%); }
  .section-title { position: absolute; top: 62px; width: 100%; text-align: center; font-family: "Poppins", Arial, sans-serif; font-weight: 600; font-size: 22px; letter-spacing: 0.5px; color: var(--ink); }
  .product-card { position: absolute; background: var(--white); }
  .product-tag { position: absolute; left: 11px; top: 12px; width: 66px; height: 17px; background: var(--steel); color: var(--white); font-family: "Oswald", Arial, sans-serif; font-weight: 500; font-size: 8px; line-height: 17px; text-align: center; }
  .product-photo { position: absolute; border-radius: 4px; }
  .product-name { position: absolute; font-family: "Poppins", Arial, sans-serif; font-weight: 500; font-size: 10.5px; color: var(--ink); }
  .product-desc { position: absolute; font-size: 7.3px; line-height: 16px; color: var(--body-text); }
  .product-price { position: absolute; font-size: 12.5px; color: #333333; }
  .buy-link { position: absolute; font-size: 7.5px; color: var(--buy-red); text-decoration: underline; }

  /* Footer */
  .site-footer { position: absolute; top: 934px; left: 0; width: 698px; height: 241px; background: var(--white); }
  .footer-brand { position: absolute; left: 290px; top: 38px; display: flex; align-items: center; gap: 6px; }
  .footer-brand .brand-mark { width: 44px; height: 44px; }
  .footer-brand .brand-name { font-size: 13px; }
  .newsletter-copy { position: absolute; top: 98px; width: 100%; text-align: center; font-family: "Poppins", Arial, sans-serif; font-size: 9.5px; line-height: 15.5px; color: var(--ink); }
  .newsletter-form { position: absolute; left: 213px; top: 142px; width: 272px; height: 30px; border: 1px solid var(--line); border-radius: 15px; }
  .newsletter-input { position: absolute; left: 14px; top: 0; font-size: 7.5px; line-height: 28px; color: #666666; }
  .newsletter-button { position: absolute; right: 3px; top: 3px; width: 69px; height: 23px; border-radius: 12px; background: var(--steel); color: var(--white); font-family: "Poppins", Arial, sans-serif; font-weight: 500; font-size: 10.5px; line-height: 23px; text-align: center; }
  .social-links { position: absolute; top: 190px; left: 277px; display: flex; gap: 6px; }
  .social-links span { width: 24px; height: 24px; border-radius: 50%; background: var(--steel-dark); }

  .legal-bar { position: absolute; top: 1175px; left: 0; width: 698px; height: 25px; background: var(--steel); color: var(--white); font-size: 6.5px; line-height: 25px; text-align: center; }
</style>
</head>
<body>
  <header class="site-header">
    <div class="brand"><span class="brand-mark"></span><span class="brand-name">PELICAN CREST</span></div>
    <nav class="main-nav">
      <a href="#">HOME</a><a href="#">PRODUCTS</a><a href="#">BLOG</a><a href="#">CONTACT US</a>
    </nav>
    <svg class="cart-icon" width="12" height="11" viewBox="0 0 12 11" aria-label="Cart">
      <path d="M0 1h2l1.6 6h6.2L11.5 2.5H3" fill="none" stroke="#333" stroke-width="1.3"/>
      <circle cx="4.5" cy="9.5" r="1" fill="#333"/><circle cx="9" cy="9.5" r="1" fill="#333"/>
    </svg>
  </header>

  <section class="hero">
    <div class="hero-photo" role="img" aria-label="Close-up of cooked pink shrimp on a plate"></div>
    <h1 class="hero-title">FROM OUR SHORE<br>TO YOUR DOOR</h1>
    <div class="hero-button">Enquire Now</div>
    <div class="slider-dots"><span class="is-active"></span><span></span><span></span><span></span></div>
  </section>

  <section class="products">
    <div class="products-backdrop" role="img" aria-label="Faded harbour with shrimp boats"></div>
    <h2 class="section-title">OUR PRODUCTS</h2>

    <article class="product-card" style="left:113px; top:105px; width:224px; height:208px;">
      <div class="product-tag">SHRIMP</div>
      <div class="product-photo" role="img" aria-label="Bowl of cooked shrimp" style="left:52px; top:28px; width:125px; height:97px; background: radial-gradient(ellipse at 50% 50%, var(--shrimp) 0%, var(--shrimp-light) 55%, var(--white) 80%);"></div>
      <div class="product-name" style="left:14px; top:128px;">US domestic shrimp</div>
      <div class="product-desc" style="left:14px; top:147px;">Sed ut perspiciatis unde omnis iste natus<br>error sit voluptatem accusantium</div>
      <div class="product-price" style="left:14px; top:185px;">$526.00</div>
      <a class="buy-link" style="left:173px; top:189px;">Buy Now</a>
    </article>

    <article class="product-card" style="left:361px; top:105px; width:224px; height:208px;">
      <div class="product-tag">SHRIMP</div>
      <div class="product-photo" role="img" aria-label="Single cooked shrimp" style="left:70px; top:34px; width:86px; height:90px; background: radial-gradient(ellipse at 50% 50%, var(--shrimp) 0%, var(--shrimp-light) 50%, var(--white) 75%);"></div>
      <div class="product-name" style="left:11px; top:128px;">Shrimp from the Gulf of Mexico</div>
      <div class="product-desc" style="left:11px; top:147px;">Sed ut perspiciatis unde omnis iste natus<br>error sit voluptatem accusantium</div>
      <div class="product-price" style="left:11px; top:185px;">$526.00</div>
      <a class="buy-link" style="left:175px; top:189px;">Buy Now</a>
    </article>

    <article class="product-card" style="left:113px; top:337px; width:472px; height:127px;">
      <div class="product-tag">SHRIMP</div>
      <div class="product-photo" role="img" aria-label="Whole raw shrimp with long antennae" style="left:55px; top:38px; width:105px; height:89px; background: radial-gradient(ellipse at 55% 45%, #7d6a4c 0%, #b8a88a 40%, var(--white) 72%);"></div>
      <div class="product-name" style="left:219px; top:34px;">US domestic shrimp</div>
      <div class="product-desc" style="left:219px; top:52px;">Sed ut perspiciatis unde omnis iste natus error sit<br>voluptatem accusantium</div>
      <div class="product-price" style="left:219px; top:89px;">$526.00</div>
      <a class="buy-link" style="left:422px; top:93px;">Buy Now</a>
    </article>
  </section>

  <footer class="site-footer">
    <div class="footer-brand"><span class="brand-mark"></span><span class="brand-name">PELICAN CREST</span></div>
    <p class="newsletter-copy">Join Our Newsletter For<br>Get More Offers</p>
    <div class="newsletter-form">
      <span class="newsletter-input">Enter Your Email Address</span>
      <span class="newsletter-button">Join Us</span>
    </div>
    <div class="social-links" aria-label="Social media links">
      <span></span><span></span><span></span><span></span><span></span>
    </div>
  </footer>

  <div class="legal-bar">© 2019 Copyrights. THE COMPANY NAME. All rights reserved. | Terms &amp; Conditions | Privacy Policy.</div>
</body>
</html>
```